Business Card Design

We are a commercial real estate brokerage in San Francisco, leasing office buildings downtown.
I would like a clean, elegant look. Simple but powerful .

Industry/Entity Type

Business

Contact Information for Business Card

Colin Farrow
lic# 07281549
415.555.0172
colin@tarvo-commercial.example
tarvo-commercial.example

```html
<!DOCTYPE html>
<html lang="en">
<head>
<meta charset="utf-8">
<title>Tarvo Commercial – Colin Farrow</title>
<link rel="stylesheet" href="https://fonts.googleapis.com/css2?family=Questrial&display=swap">
<style>
  :root {
    --card-bg: #ffffff;
    --ink: #111111;
    --slate: #7b8ba8;
    --mark-grey: #8c8c8c;
    --divider: #555555;
    --band-text: #ffffff;
  }
  html, body {
    margin: 0;
    padding: 0;
    overflow: hidden;
    background: var(--card-bg);
  }
  .card {
    position: relative;
    width: 1200px;
    height: 703px;
    background: var(--card-bg);
    font-family: "Questrial", "Century Gothic", sans-serif;
    color: var(--ink);
    overflow: hidden;
  }
  .brand-mark {
    position: absolute;
    left: 70px;
    top: 70px;
    width: 120px;
    height: 120px;
    background: var(--mark-grey);
  }
  .brand-divider {
    position: absolute;
    left: 244px;
    top: 47px;
    width: 3px;
    height: 152px;
    background: var(--divider);
  }
  .brand-name {
    position: absolute;
    left: 264px;
    top: 52px;
    margin: 0;
    color: var(--slate);
    font-weight: 400;
    line-height: 1;
  }
  .brand-name .primary {
    display: block;
    font-size: 94px;
    letter-spacing: 2px;
  }
  .brand-name .secondary {
    display: block;
    font-size: 40px;
    letter-spacing: 1px;
    margin-top: 4px;
  }
  .license {
    position: absolute;
    right: 28px;
    top: 38px;
    font-size: 30px;
  }
  .person-name {
    position: absolute;
    left: 0;
    right: 0;
    top: 326px;
    margin: 0;
    text-align: center;
    font-size: 47px;
    font-weight: 400;
  }
  .contact-line {
    position: absolute;
    left: 0;
    right: 0;
    top: 530px;
    text-align: center;
    font-size: 31px;
  }
  .contact-line .sep {
    margin: 0 22px;
  }
  .web-band {
    position: absolute;
    left: 23px;
    top: 614px;
    width: 1154px;
    height: 50px;
    background: var(--slate);
    color: var(--band-text);
    font-size: 28px;
    line-height: 50px;
    text-align: center;
  }
</style>
</head>
<body>
  <div class="card">
    <div class="brand-mark"></div>
    <div class="brand-divider"></div>
    <h1 class="brand-name">
      <span class="primary">TARVO</span>
      <span class="secondary">COMMERCIAL</span>
    </h1>
    <div class="license">License# 07281549</div>

    <h2 class="person-name">Colin Farrow</h2>

    <div class="contact-line">
      <span class="phone">Cell: 415 555 0172</span><span class="sep">|</span><span class="email">Email: colin@tarvo-commercial.example</span>
    </div>

    <div class="web-band">www.tarvo-commercial.example</div>
  </div>
</body>
</html>
```